Website design for an events management company

What we need is the design of a website to be used by an events management company, the company is called "Velto Conference Services" and the website is expected to contain the following sections:
1) Homepage
2) Who are we?
3) Mission / Vision / Core values
4) Why to choose Velto?
5) Past experience
6) Duties or provided services (Scientific Program Duties, Accreditation, Fund Raising, Accommodations, Social Activities, Transportation, Marketing of the Event, Publications and printed materials, Secretarial Work and Media Coverage)
7) References
8) Contact Us page (will probably contain a contact us form plus email, address and a google map)

Attached for your reference the company's logo

Expected that the winner should deliver the designs of at least two pages (the homepage plus an inner page) plus of course all the used graphics, images ... etc.

Thanks

Target Market(s)

The design need to target scientific events and not public events, for example the company doesn't organize music concerts ... etc., it organizes only scientific events so please target business users (i.e. doctors, engineers, scientisits ... etc) while making the designs, including the correct colors, images and icons

Industry/Entity Type

It Company

Number of Pages Required

2 page

Requirements
Must have
• One homepage
• One inner page
• All the used graphics and images
Nice to have
• More than two pages

```html
<!DOCTYPE html>
<html lang="en">
<head>
<meta charset="utf-8">
<title>Velto Conference Services</title>
<link href="https://fonts.googleapis.com/css2?family=Questrial&family=Arimo:wght@400;700&display=swap" rel="stylesheet">
<style>
:root{
  --blue:#29a8e0;
  --blue-dark:#1f8fc4;
  --ink:#222;
  --text:#555;
  --muted:#777;
  --light:#fff;
  --dark-band:#333;
  --footer:#222;
  --rule:#e4e4e4;
  --accent-red:#d9232d;
  --icon-grey:#9a9a9a;
}
*{margin:0;padding:0;box-sizing:border-box}
html,body{width:1200px;height:3333px;overflow:hidden}
body{position:relative;background:var(--light);font-family:"Arimo",Arial,sans-serif;color:var(--text)}
.abs{position:absolute}
.heading{font-family:"Questrial",sans-serif;font-weight:400;color:var(--ink)}
.hatch{height:12px;background:repeating-linear-gradient(135deg,#ddd 0 2px,transparent 2px 5px)}
.hatch--dark{background:repeating-linear-gradient(135deg,#888 0 2px,transparent 2px 5px)}
.btn{display:flex;align-items:center;justify-content:center;background:var(--blue);color:#fff;
  font-family:"Questrial",sans-serif;font-size:19px;border-radius:28px;letter-spacing:.5px}
.photo{position:absolute}

/* hero */
.hero{left:0;top:0;width:1200px;height:596px;
  background:linear-gradient(180deg,#e7e5e1 0%,#cfcac3 45%,#7d6a58 62%,#3e3a38 80%,#2a2a2c 100%)}
.hero__screen{left:318px;top:24px;width:546px;height:330px;background:linear-gradient(135deg,#fafcfd,#dfeaf1);
  border:14px solid #b9b9b9;display:flex;align-items:center;justify-content:center}
.hero__name{font-family:"Questrial",sans-serif;font-size:46px;color:#555}
.nav{left:0;top:596px;width:1200px;height:57px;background:linear-gradient(180deg,#31b1e6,#1f98d2);
  display:flex;align-items:center;justify-content:center;gap:0}
.nav a{color:#fff;text-decoration:none;font-family:"Questrial",sans-serif;font-size:17px;padding:0 14px}
.nav span{color:#fff;font-size:17px}

/* who */
.section-title{left:0;width:1200px;text-align:center;font-size:31px}
.section-title em{font-style:normal;color:var(--blue)}
.lead{left:290px;width:620px;text-align:center;font-size:14.5px;line-height:24px;color:var(--text)}
.feature{width:230px;text-align:center}
.feature__icon{width:116px;height:116px;margin:0 auto}
.feature__name{font-family:"Questrial",sans-serif;font-size:19px;color:var(--ink);margin-top:34px}
.feature--active .feature__name{color:var(--blue)}
.feature__text{font-size:13.5px;line-height:23px;color:var(--text);margin-top:16px}

/* quote */
.quote{left:0;top:1200px;width:1200px;height:413px;
  background:radial-gradient(ellipse at 70% 60%,#b28a5f 0%,#7a5a40 35%,#3a3340 70%,#22242c 100%)}
.quote__text{left:0;top:1350px;width:1200px;text-align:center;color:#fff;font-family:"Questrial",sans-serif;font-size:37px;line-height:53px}
.quote__mark{color:#fff;font-family:"Questrial",sans-serif;font-size:90px;line-height:1}
.quote__by{left:0;top:1498px;width:1200px;text-align:center;color:#fff;font-size:19px;font-family:"Questrial",sans-serif}
.quote__by b{font-family:"Arimo",sans-serif}
.quote__brand{left:0;top:1280px;width:1200px;text-align:center;color:#fff;font-family:"Questrial",sans-serif;font-size:20px}

/* blocks */
.block-title{font-size:31px}
.block-text{font-size:13.5px;line-height:23px;color:var(--text)}
.vision{left:0;top:1978px;width:1200px;height:364px;background:var(--dark-band)}
.vision .block-title{color:#fff}
.vision .block-text{color:#8a8a8a;text-align:right}
.values{list-style:none;font-size:14px;line-height:30.4px;color:var(--text)}
.values b{color:var(--accent-red)}

/* subscribe */
.subscribe{left:0;top:2771px;width:1200px;height:458px;
  background:linear-gradient(110deg,#5b4a3c 0%,#8e7866 30%,#b7a89a 55%,#8a8c96 80%,#5d6470 100%)}
.field{left:382px;width:436px;height:40px;border-radius:20px;background:rgba(255,255,255,.35);
  color:#fff;font-size:14px;display:flex;align-items:center;justify-content:center}
.footer{left:0;top:3229px;width:1200px;height:104px;background:var(--footer)}
.social{width:31px;height:31px;border:2px solid #8a8a8a}
.social--blue{border-color:var(--blue)}
.copyright{left:0;top:3296px;width:1200px;text-align:center;color:#ddd;font-size:14px}
.copyright span{color:var(--blue)}
</style>
</head>
<body>

<!-- Hero -->
<div class="abs hero" role="img" aria-label="Photo of a boardroom meeting with people seated around a table facing a wall screen"></div>
<div class="abs hero__screen"><span class="hero__name">Velto</span></div>
<nav class="abs nav">
  <a>Home</a><span>:</span><a>Who are we?</a><span>:</span><a>Mission</a><span>:</span><a>Why to choose Velto?</a><span>:</span><a>Past experience</a><span>:</span><a>Duties</a><span>:</span><a>References</a><span>:</span><a>Contact Us</a>
</nav>

<!-- Who is -->
<div class="abs hatch" style="left:167px;top:718px;width:330px"></div>
<div class="abs hatch" style="left:703px;top:718px;width:330px"></div>
<h2 class="abs heading section-title" style="top:702px">Who is <em>VELTO</em></h2>
<p class="abs lead" style="top:758px">Being positive is our commitment to making a positive difference in the world.Through redesigning the way we work and live.</p>

<div class="abs feature feature--active" style="left:89px;top:832px">
  <svg class="feature__icon" viewBox="0 0 116 116">
    <circle cx="58" cy="58" r="55" fill="#fff" stroke="var(--blue)" stroke-width="5"/>
    <circle cx="58" cy="58" r="45" fill="var(--blue)"/>
    <g fill="none" stroke="#fff" stroke-width="2.5">
      <ellipse cx="58" cy="58" rx="25" ry="9"/>
      <ellipse cx="58" cy="58" rx="25" ry="9" transform="rotate(60 58 58)"/>
      <ellipse cx="58" cy="58" rx="25" ry="9" transform="rotate(-60 58 58)"/>
    </g>
    <circle cx="58" cy="58" r="4" fill="#fff"/>
  </svg>
  <div class="feature__name">Scientific Program</div>
  <p class="feature__text">Lorem ipsum is simply dummy text of the printing and typesetting industry.</p>
</div>

<div class="abs feature" style="left:352px;top:832px">
  <svg class="feature__icon" viewBox="0 0 116 116">
    <circle cx="58" cy="58" r="55" fill="#fff" stroke="#c9c9c9" stroke-width="5"/>
    <circle cx="58" cy="58" r="45" fill="var(--icon-grey)"/>
    <rect x="42" y="34" width="32" height="44" fill="#fff"/>
    <g stroke="var(--icon-grey)" stroke-width="2.5"><line x1="48" y1="44" x2="68" y2="44"/><line x1="48" y1="52" x2="68" y2="52"/><line x1="48" y1="60" x2="62" y2="60"/></g>
    <circle cx="64" cy="70" r="5" fill="var(--icon-grey)"/>
  </svg>
  <div class="feature__name">Accreditation</div>
  <p class="feature__text">Lorem ipsum is simply dummy text of the printing and typesetting industry.</p>
</div>

<div class="abs feature" style="left:616px;top:832px">
  <svg class="feature__icon" viewBox="0 0 116 116">
    <circle cx="58" cy="58" r="55" fill="#fff" stroke="#c9c9c9" stroke-width="5"/>
    <circle cx="58" cy="58" r="45" fill="var(--icon-grey)"/>
    <circle cx="58" cy="48" r="14" fill="#fff"/>
    <text x="58" y="54" text-anchor="middle" font-family="Arimo,sans-serif" font-weight="700" font-size="17" fill="var(--icon-grey)">$</text>
    <path d="M34 62 L46 72 L58 76 L70 72 L82 62 L82 70 L70 82 L46 82 L34 70 Z" fill="#fff"/>
  </svg>
  <div class="feature__name">Fund Raising</div>
  <p class="feature__text">Lorem ipsum is simply dummy text of the printing and typesetting industry.</p>
</div>

<div class="abs feature" style="left:880px;top:832px">
  <svg class="feature__icon" viewBox="0 0 116 116">
    <circle cx="58" cy="58" r="55" fill="#fff" stroke="#c9c9c9" stroke-width="5"/>
    <circle cx="58" cy="58" r="45" fill="var(--icon-grey)"/>
    <path d="M30 66 L34 54 L52 54 L56 66 Z" fill="#fff"/>
    <rect x="28" y="64" width="30" height="8" fill="#fff"/>
    <rect x="62" y="46" width="28" height="26" rx="3" fill="#fff"/>
    <rect x="66" y="50" width="20" height="8" fill="var(--icon-grey)"/>
    <g fill="#fff"><circle cx="36" cy="74" r="4"/><circle cx="50" cy="74" r="4"/><circle cx="68" cy="74" r="4"/><circle cx="84" cy="74" r="4"/></g>
  </svg>
  <div class="feature__name">Transportation</div>
  <p class="feature__text">Lorem ipsum is simply dummy text of the printing and typesetting industry.</p>
</div>

<div class="abs btn" style="left:506px;top:1093px;width:189px;height:51px">LEARN MORE</div>

<!-- Quote -->
<div class="abs quote" role="img" aria-label="Photo of a man from behind facing a blurred conference audience"></div>
<div class="abs quote__brand">Velto</div>
<div class="abs quote__mark" style="left:172px;top:1340px">“</div>
<div class="abs quote__mark" style="left:992px;top:1398px">”</div>
<p class="abs quote__text">The Price of Greatness is Responsibility Over<br>each of Your Thoughts</p>
<p class="abs quote__by"><b>VELTO</b> Conference Services</p>

<!-- Mission -->
<div class="photo" style="left:133px;top:1667px;width:438px;height:257px;background:linear-gradient(180deg,#e9edf0 0%,#c9d0d6 50%,#5b6068 100%)" role="img" aria-label="Photo of a bright open-plan office with desks and staff"></div>
<h2 class="abs heading block-title" style="left:607px;top:1660px">Mission</h2>
<div class="abs hatch" style="left:732px;top:1676px;width:335px"></div>
<p class="abs block-text" style="left:607px;top:1708px;width:460px">To distinguish ourselves in the event management market by managing, producing and supporting outstanding events that exceed customers increasing expectations in terms of value, service and innovation.</p>
<div class="abs btn" style="left:604px;top:1873px;width:187px;height:51px">LEARN MORE</div>

<!-- Vision -->
<div class="abs vision"></div>
<div class="abs hatch hatch--dark" style="left:133px;top:2040px;width:352px"></div>
<h2 class="abs heading block-title" style="left:497px;top:2025px;color:#fff">Vision</h2>
<p class="abs block-text" style="left:133px;top:2074px;width:454px;color:#8a8a8a;text-align:right">We will strive to be seen as leaders and innovators in the event management industry. We will surpass the expectations of our clients with our honest dedication to producing and managing outstanding events. We will gain the trust and respect of our clients and our staff by never compromising our values. We will show genuine concern for the success of our events.</p>
<div class="abs btn" style="left:400px;top:2238px;width:187px;height:51px">LEARN MORE</div>
<div class="photo" style="left:624px;top:2029px;width:438px;height:260px;background:linear-gradient(90deg,#e8ecec 0%,#cfd6d2 45%,#6b5448 60%,#dfe3e1 100%)" role="img" aria-label="Photo of a smiling businesswoman in a dark suit"></div>

<!-- Core Values -->
<div class="abs hatch" style="left:140px;top:2405px;width:345px"></div>
<div class="abs hatch" style="left:715px;top:2405px;width:345px"></div>
<h2 class="abs heading section-title" style="top:2389px">Core Values</h2>
<div class="photo" style="left:133px;top:2451px;width:438px;height:260px;background:linear-gradient(180deg,#3a3e44 0%,#8c9096 35%,#4a4644 70%,#2a2a2c 100%)" role="img" aria-label="Photo of a panel discussion on stage in front of a seated audience"></div>
<ul class="abs values" style="left:607px;top:2443px;width:520px">
  <li><b>W</b>e use our platform as business leaders to draw attention to society causes.</li>
  <li><b>E</b>stablishing long-term relations with our customers.</li>
  <li><b>R</b>esponsibility towards the community.</li>
  <li><b>E</b>stablishing a Life-long Learning.</li>
  <li><b>S</b>urpassing obstacles.</li>
  <li><b>P</b>ositive ambition.</li>
  <li><b>E</b>agerness to innovate.</li>
  <li><b>C</b>ustomer Satisfaction.</li>
  <li><b>T</b>aking a leadership role in shaping the event management industry.</li>
</ul>

<!-- Subscribe -->
<div class="abs subscribe" role="img" aria-label="Photo of business colleagues talking in a meeting"></div>
<div class="abs hatch" style="left:500px;top:2820px;width:200px;background:repeating-linear-gradient(135deg,#fff 0 2px,transparent 2px 5px)"></div>
<h2 class="abs heading section-title" style="top:2848px;color:#fff">VELTO Conference Services</h2>
<p class="abs" style="left:0;top:2903px;width:1200px;text-align:center;color:#fff;font-size:14.5px">Lorem Ipsum is simply dummy text of the printing and typesetting industry.</p>
<div class="abs field" style="top:2984px">Your Name</div>
<div class="abs field" style="top:3035px">Your E-Mail</div>
<div class="abs btn" style="left:382px;top:3100px;width:436px;height:40px;border-radius:20px;font-size:17px">SUBSCRIBE</div>
<svg class="abs" style="left:588px;top:3195px" width="24" height="24" viewBox="0 0 24 24" fill="none" stroke="#fff" stroke-width="3"><path d="M4 12 L12 4 L20 12"/><path d="M4 21 L12 13 L20 21"/></svg>

<!-- Footer -->
<footer class="abs footer"></footer>
<div class="abs social social--blue" style="left:541px;top:3246px"></div>
<div class="abs social" style="left:584px;top:3246px"></div>
<div class="abs social" style="left:627px;top:3246px"></div>
<p class="abs copyright">© <span>Velto Conference Services</span> - 2015. All Rights Reserved.</p>

</body>
</html>
```